Vellora Labs - Mushroom Supplement Packaging

Our brand is called Vellora Labs. I've added a couple different logos that you can use. We are creating a line up of Mushroom Supplement products. I will add the entire line-up of products here. I've added examples of other products and packaging shape types I can purchase. Give me different options for packaging that is minimalist and clean for this brand that makes it look really well made and clean and make people want to buy.

Product 1 Lions Mane 1g
Product 2 Cordyceps 1g
Product 3 Chaga 1g
Product 4 Turkey Tail 1g
Product 5 Reishi 1g
Product 6 Maitake 1g
Product 7 Shiitake 1g

Product 8 (Mix) Lions Mane 143mg
Cordyceps 143mg
Chaga 143mg
Turkey Tail 143mg
Reishi 143mg
Maitake 143mg
Shiitake 143mg

```html
<!DOCTYPE html>
<html lang="en">
<head>
<meta charset="utf-8">
<title>Vellora Labs – Lion's Mane Mushroom Supplement Label</title>
<link href="https://fonts.googleapis.com/css2?family=Bebas+Neue&family=Montserrat:wght@400;600&display=swap" rel="stylesheet">
<style>
  :root {
    --backdrop: #eeeeee;
    --label: #ffffff;
    --label-shade: #e4e4e4;
    --brand-blue: #4485bd;
    --brand-blue-soft: #e9eff7;
    --ink: #1b1b1b;
    --muted: #8a8a8a;
    --rule: #9a9a9a;
  }
  * { margin: 0; padding: 0; box-sizing: border-box; }
  html, body {
    width: 1200px;
    height: 800px;
    overflow: hidden;
    background: var(--backdrop);
  }
  .label {
    position: absolute;
    left: 230px;
    top: 45px;
    width: 740px;
    height: 710px;
    background: linear-gradient(90deg, var(--label) 0%, var(--label) 30%, var(--label-shade) 100%);
    overflow: hidden;
    font-family: "Montserrat", sans-serif;
  }
  .label__artwork {
    position: absolute;
    left: -20px;
    top: 25px;
    width: 390px;
    height: 680px;
    border-radius: 48% 52% 40% 45%;
    background: radial-gradient(ellipse at 55% 45%, rgba(233,239,247,0.2) 0%, var(--brand-blue-soft) 70%, rgba(233,239,247,0) 100%);
  }
  .brand {
    position: absolute;
    left: 277px;
    top: 26px;
    width: 190px;
    display: flex;
    align-items: center;
    gap: 9px;
  }
  .brand__dot {
    flex: none;
    width: 12px;
    height: 12px;
    border-radius: 50%;
    background: var(--brand-blue);
  }
  .brand__name {
    font-weight: 600;
    font-size: 27px;
    line-height: 31px;
    letter-spacing: 1px;
    text-transform: uppercase;
    color: var(--ink);
  }
  .dose-badge {
    position: absolute;
    left: 549px;
    top: 0;
    width: 103px;
    height: 108px;
    background: var(--brand-blue);
    color: #fff;
    text-align: center;
  }
  .dose-badge__amount {
    display: block;
    font-family: "Bebas Neue", sans-serif;
    font-size: 58px;
    line-height: 1;
    padding-top: 10px;
  }
  .dose-badge__unit {
    display: block;
    font-size: 22px;
    line-height: 1;
    margin-top: 4px;
  }
  .product-type {
    position: absolute;
    left: 300px;
    top: 262px;
    font-weight: 600;
    font-size: 52px;
    line-height: 56px;
    letter-spacing: 1px;
    color: var(--brand-blue);
  }
  .product-type__rule {
    position: absolute;
    left: 302px;
    top: 383px;
    width: 378px;
    height: 2px;
    background: var(--rule);
  }
  .benefits {
    position: absolute;
    left: 302px;
    top: 394px;
    list-style: none;
    font-size: 14px;
    line-height: 24.5px;
    letter-spacing: 0.8px;
    color: var(--muted);
  }
  .product-name {
    position: absolute;
    left: 52px;
    top: 525px;
  }
  .product-name text {
    font-family: "Bebas Neue", sans-serif;
    font-size: 240px;
    fill: var(--brand-blue);
  }
</style>
</head>
<body>
  <main class="label">
    <div class="label__artwork" role="img" aria-label="Faint line illustration of a lion's head with flowing mane"></div>

    <div class="brand">
      <span class="brand__dot"></span>
      <span class="brand__name">Vellora<br>Labs</span>
    </div>

    <div class="dose-badge">
      <span class="dose-badge__amount">1</span>
      <span class="dose-badge__unit">G</span>
    </div>

    <h2 class="product-type">MUSHROOM<br>SUPPLEMENT</h2>
    <div class="product-type__rule"></div>

    <ul class="benefits">
      <li>SUPPORTS A HEALTHY IMMUNE SYSTEM</li>
      <li>SUPPORTS OVERALL WELL-BEING</li>
      <li>BRAIN BOOSTER</li>
    </ul>

    <svg class="product-name" width="640" height="180" viewBox="0 0 640 180">
      <text x="0" y="174" textLength="632" lengthAdjust="spacingAndGlyphs">LION'S MANE</text>
    </svg>
  </main>
</body>
</html>
```